Rivet Halvora needs a new Website Design

We need a WEB site landing page (/template) design, we currently have a company logo.We like the Tarvex.com web designEnclosed is our company logo.Our Current website is https://www.rivethalvora.com.au/

Number of Pages Required

1 page

```html
<!DOCTYPE html>
<html lang="en">
<head>
<meta charset="utf-8">
<title>Rivet Halvora — Advanced Simplicity</title>
<link href="https://fonts.googleapis.com/css2?family=Poppins:wght@300;400;500;600;700;800&display=swap" rel="stylesheet">
<style>
:root{
  --blue:#1b8fd8;
  --blue-dark:#0f6fb8;
  --ink:#1d2735;
  --text:#4c5563;
  --muted:#8a93a0;
  --line:#e3e8ee;
  --pale:#eef6fd;
  --footer:#1e2330;
  --white:#ffffff;
}
*{box-sizing:border-box;margin:0;padding:0}
html,body{width:1200px;height:5333px;overflow:hidden}
body{font-family:'Poppins',sans-serif;color:var(--ink);background:var(--white);position:relative}
.abs{position:absolute}
a{color:inherit;text-decoration:none}

/* hero */
.hero{position:absolute;left:0;top:0;width:1200px;height:677px;overflow:hidden}
.hero-photo{position:absolute;inset:0;background:linear-gradient(120deg,#3c4350 0%,#6b6258 40%,#4a4c55 70%,#2d333f 100%)}
.hero-shade{position:absolute;inset:0;background:rgba(20,26,38,.35)}
.topbar{position:absolute;left:89px;right:89px;top:6px;height:20px;display:flex;align-items:center;font-size:11px;font-weight:600;color:var(--white)}
.topbar .flag{width:14px;height:14px;border-radius:50%;background:#c8d3e6;margin-right:8px}
.topbar .dots{display:flex;gap:12px;margin-left:30px}
.topbar .dots span{width:9px;height:9px;border-radius:50%;background:var(--white)}
.topbar .right{margin-left:auto;display:flex;gap:40px}
.nav{position:absolute;left:89px;right:89px;top:58px;height:60px;display:flex;align-items:center}
.brand{display:flex;align-items:center;gap:10px;color:var(--white);font-size:25px;font-weight:300}
.brand .mark{width:22px;height:22px;border-radius:50%;background:var(--blue)}
.menu{margin-left:auto;display:flex;gap:34px;font-size:11px;font-weight:600;color:var(--white);align-items:center}
.menu .search{width:26px;height:26px;border-radius:50%;border:1px solid rgba(255,255,255,.7)}
.hero h1{position:absolute;left:0;right:0;top:235px;text-align:center;color:var(--white);font-weight:700;font-size:88px;line-height:1}
.hero h2{position:absolute;left:0;right:0;top:330px;text-align:center;color:var(--white);font-weight:700;font-size:66px;line-height:1}
.hero p{position:absolute;left:0;right:0;top:413px;text-align:center;color:var(--white);font-size:17px}
.hero .btns{position:absolute;left:0;right:0;top:462px;display:flex;justify-content:center;gap:4px}
.btn{display:inline-flex;align-items:center;justify-content:center;font-size:11px;font-weight:600;letter-spacing:.3px;height:44px;padding:0 24px}
.btn-blue{background:var(--blue);color:var(--white)}
.btn-ghost{background:rgba(255,255,255,.18);color:var(--white)}
.btn-line{border:1px solid var(--line);color:var(--ink);background:var(--white);box-shadow:0 2px 6px rgba(0,0,0,.06)}
.play{position:absolute;left:1068px;top:370px}

.section-title{position:absolute;left:0;right:0;text-align:center;font-size:38px;font-weight:600;color:var(--ink)}
.dots-row{position:absolute;left:0;right:0;display:flex;justify-content:center;gap:8px}
.dots-row span{width:10px;height:10px;border-radius:50%;border:1.5px solid #9aa3ae}
.dots-row span.on{background:#333;border-color:#333}

/* news */
.news-card{position:absolute;top:830px;width:322px;height:380px;overflow:visible}
.news-card .img{position:absolute;inset:0}
.news-card h3{position:absolute;left:44px;bottom:28px;color:var(--white);font-size:16px;font-weight:600;line-height:1.5}
.news-card .arrow{position:absolute;right:-4px;bottom:-22px;width:58px;height:58px;border-radius:50%;background:var(--white);box-shadow:0 3px 10px rgba(0,0,0,.15);display:flex;align-items:center;justify-content:center}

/* offer */
.offer{position:absolute;left:0;top:1339px;width:1200px;height:647px;background:var(--pale)}
.offer .sub{position:absolute;left:0;right:0;top:127px;text-align:center;font-size:13px;color:var(--text)}
.offer .circle{position:absolute;left:402px;top:173px;width:396px;height:396px;border-radius:50%;background:linear-gradient(135deg,#c9b8a6,#7c6b61 55%,#3b3a42)}
.offer-item{position:absolute;display:flex;align-items:center;gap:10px;font-size:15px;font-weight:600;color:var(--blue-dark)}
.offer-item.right{text-align:right}

/* products */
.shot{position:absolute;width:505px;background:var(--white);border-radius:8px;box-shadow:0 8px 30px rgba(20,40,70,.14);padding:14px}
.shot .wdots{display:flex;gap:6px;margin-bottom:10px}
.shot .wdots i{width:10px;height:10px;border-radius:50%}
.shot .wdots i:nth-child(1){background:#ef4b4b}
.shot .wdots i:nth-child(2){background:#f5b731}
.shot .wdots i:nth-child(3){background:#3ec150}
.shot .screen{width:100%;border-radius:4px}
.badge{position:absolute;width:164px;height:164px;border-radius:50%;background:var(--white);box-shadow:0 8px 26px rgba(20,40,70,.16);display:flex;align-items:center;justify-content:center}
.prod-text{position:absolute;width:410px}
.prod-text h3{font-size:27px;font-weight:600;color:var(--ink);line-height:1.2}
.prod-text .tag{font-size:14px;color:var(--muted);margin-top:4px}
.prod-text p{font-size:12px;line-height:1.7;color:var(--text);margin-top:26px}
.prod-text p + p{margin-top:14px}
.prod-text .btn{margin-top:20px;height:46px}

/* support */
.support{position:absolute;left:0;top:3821px;width:1200px;height:228px;background:linear-gradient(90deg,#1286d3,#29a8ec 55%,#1591db)}
.support h2{position:absolute;left:89px;top:64px;color:var(--white);font-size:40px;font-weight:600}
.support h2 small{font-size:12px;font-weight:600;margin-left:8px}
.support p{position:absolute;left:89px;top:128px;width:560px;color:var(--white);font-size:14px;line-height:1.6}
.support .btn{position:absolute;left:908px;top:88px;height:54px;background:var(--white);color:var(--ink);padding:0 20px}

/* why */
.why-item{position:absolute;width:500px;display:flex;gap:22px}
.why-item svg{flex:none}
.why-item h4{font-size:16px;font-weight:600;color:var(--ink)}
.why-item p{font-size:12px;line-height:1.75;color:var(--text);margin-top:12px}

/* hardware */
.hw{position:absolute;top:4655px;font-size:28px;color:#9aa0a8;font-weight:500;transform:translateX(-50%);white-space:nowrap}

/* footer */
.footer{position:absolute;left:0;top:4831px;width:1200px;height:502px;background:var(--footer);color:#c6cbd4}
.footer .flogo{position:absolute;left:89px;top:168px;display:flex;align-items:center;gap:12px;color:var(--white);font-size:32px;font-weight:300}
.footer .flogo .mark{width:30px;height:30px;border-radius:50%;background:var(--blue)}
.footer .fsoc{position:absolute;left:145px;top:250px;display:flex;gap:14px}
.footer .fsoc span{width:30px;height:30px;border-radius:50%;border:1px solid #5d6473}
.fcol{position:absolute;top:94px;font-size:12px;line-height:27px}
.fcol h5{font-size:16px;font-weight:600;color:var(--white);margin-bottom:18px;line-height:1.2}
.fcol h6{font-size:12px;font-weight:600;color:var(--white);line-height:1.4;margin-top:14px}
.fcol h6:first-of-type{margin-top:0}
.fcol .c{display:flex;gap:8px;align-items:center;line-height:18px}
.fcol .c i{width:9px;height:9px;background:var(--blue);border-radius:2px;flex:none}
.footer .copy{position:absolute;left:0;right:0;top:457px;text-align:center;font-size:11px}
.totop{position:absolute;left:1130px;top:401px;width:44px;height:44px;border-radius:50%;background:var(--blue);display:flex;align-items:center;justify-content:center}
</style>
</head>
<body>

<header class="hero">
  <div class="hero-photo" role="img" aria-label="Photo of smiling business colleagues in an office"></div>
  <div class="hero-shade"></div>
  <div class="topbar">
    <span class="flag"></span>Call Us ⌄
    <div class="dots"><span></span><span></span><span></span><span></span></div>
    <div class="right"><a>SUPPORT</a><a>LOGIN</a><a>BLOG</a></div>
  </div>
  <nav class="nav">
    <div class="brand"><span class="mark"></span>Rivet Halvora</div>
    <div class="menu"><a>VOICE</a><a>DATA</a><a>HARDWARE</a><a>SERVICES REQUEST</a><a>TERMS &amp; CONDITIONS</a><a>STATUS</a><span class="search"></span></div>
  </nav>
  <h1>Advanced</h1>
  <h2>Simplicity</h2>
  <p>Australia's Business Grade Unified Communications Company</p>
  <div class="btns"><a class="btn btn-blue">LEARN MORE</a><a class="btn btn-ghost">REQUEST A DEMO</a></div>
  <svg class="play" width="20" height="22" viewBox="0 0 20 22"><path d="M2 2 L18 11 L2 20Z" fill="#fff"/></svg>
</header>

<h2 class="section-title" style="top:756px">What’s New</h2>
<article class="news-card" style="left:89px">
  <div class="img" role="img" aria-label="Photo of a support agent wearing a headset" style="background:linear-gradient(160deg,#d9dde2,#9aa6b2 60%,#5b6676)"></div>
  <h3>Whats is personal<br>dialer?</h3>
  <span class="arrow"><svg width="20" height="14" viewBox="0 0 20 14"><path d="M1 7H18M12 1L18 7L12 13" stroke="#1d2735" stroke-width="2" fill="none"/></svg></span>
</article>
<article class="news-card" style="left:439px">
  <div class="img" role="img" aria-label="Photo of a man on a phone call holding a coffee cup" style="background:linear-gradient(160deg,#b7a493,#7b6452 55%,#3e3530)"></div>
  <h3>Advantages of hiring<br>remote works</h3>
  <span class="arrow"><svg width="20" height="14" viewBox="0 0 20 14"><path d="M1 7H18M12 1L18 7L12 13" stroke="#1d2735" stroke-width="2" fill="none"/></svg></span>
</article>
<article class="news-card" style="left:789px">
  <div class="img" role="img" aria-label="Photo of young colleagues working together at a laptop" style="background:linear-gradient(160deg,#a9b2bb,#6b7684 55%,#363d49)"></div>
  <h3>UCaas for your millennial<br>employees</h3>
  <span class="arrow"><svg width="20" height="14" viewBox="0 0 20 14"><path d="M1 7H18M12 1L18 7L12 13" stroke="#1d2735" stroke-width="2" fill="none"/></svg></span>
</article>
<div class="dots-row" style="top:1255px"><span class="on"></span><span></span><span></span></div>

<section class="offer">
  <h2 class="section-title" style="top:72px">What We Offer</h2>
  <p class="sub">We have all the components to start and run your own White Label Telco</p>
  <div class="circle" role="img" aria-label="Photo of two women smiling at a laptop"></div>
  <div class="offer-item right" style="left:240px;top:176px">Cloud IP PBX
    <svg width="76" height="70" viewBox="0 0 76 70" fill="none" stroke="#1b8fd8" stroke-width="2"><path d="M18 36a12 12 0 0 1 4-23 16 16 0 0 1 30 3 10 10 0 0 1 4 20Z"/><path d="M38 36v14M20 50h36M20 50v10M38 50v10M56 50v10"/><circle cx="20" cy="63" r="3"/><circle cx="38" cy="63" r="3"/><circle cx="56" cy="63" r="3"/></svg></div>
  <div class="offer-item" style="left:778px;top:176px">
    <svg width="70" height="70" viewBox="0 0 70 70" fill="none" stroke="#1b8fd8" stroke-width="2"><rect x="24" y="6" width="22" height="16"/><path d="M35 22v12M12 34h46M12 34v10M35 34v10M58 34v10"/><rect x="4" y="44" width="16" height="14"/><rect x="27" y="44" width="16" height="14"/><rect x="50" y="44" width="16" height="14"/></svg>Data Services</div>
  <div class="offer-item right" style="left:160px;top:326px;line-height:1.35">Unified<br>Communications
    <svg width="70" height="70" viewBox="0 0 70 70" fill="none" stroke="#1b8fd8" stroke-width="2"><rect x="20" y="8" width="44" height="32" rx="2"/><path d="M14 50h52"/><rect x="6" y="24" width="18" height="34" rx="3"/></svg></div>
  <div class="offer-item" style="left:826px;top:338px">
    <svg width="62" height="62" viewBox="0 0 62 62" fill="none" stroke="#1b8fd8" stroke-width="2"><path d="M8 16h10v30H8zM18 22l14-10v38L18 40"/><path d="M40 20l14-8M40 31h16M40 42l14 8"/></svg>Voice Services</div>
  <div class="offer-item right" style="left:190px;top:484px;line-height:1.35">Invoice &amp; Payment<br>Platform
    <svg width="70" height="70" viewBox="0 0 70 70" fill="none" stroke="#1b8fd8" stroke-width="2"><rect x="24" y="8" width="38" height="26" rx="3" transform="rotate(-15 43 21)"/><path d="M8 62l10-24 14-4 10 8-18 6-6 16z"/></svg></div>
  <div class="offer-item" style="left:776px;top:496px">
    <svg width="70" height="70" viewBox="0 0 70 70" fill="none" stroke="#1b8fd8" stroke-width="2"><circle cx="35" cy="35" r="20"/><circle cx="35" cy="35" r="6" fill="#1b8fd8"/><path d="M35 4v16M35 50v16M4 35h16M50 35h16"/></svg>Support</div>
</section>

<h2 class="section-title" style="top:2066px">Our Product</h2>

<div class="shot" style="left:80px;top:2178px">
  <div class="wdots"><i></i><i></i><i></i></div>
  <div class="screen" role="img" aria-label="Screenshot of the PBX system dashboard" style="height:248px;background:linear-gradient(90deg,#4aa8e6 0 10%,#f1f4f7 10%)"></div>
</div>
<div class="badge" style="left:476px;top:2432px"><svg width="96" height="90" viewBox="0 0 96 90" fill="none" stroke="#1d2735" stroke-width="2.5"><path d="M24 44a15 15 0 0 1 5-29 20 20 0 0 1 38 4 13 13 0 0 1 5 25Z"/><path d="M48 44v16M22 60h52M22 60v10M48 60v10M74 60v10"/><rect x="14" y="70" width="16" height="12"/><rect x="40" y="70" width="16" height="12"/><rect x="66" y="70" width="16" height="12"/></svg></div>
<div class="prod-text" style="left:704px;top:2228px">
  <h3>Cloud IP PBX</h3>
  <div class="tag">Multiple IP PBXs on a single instance</div>
  <p>A Multi-Tenant CloudPBX is able to handle multiple customers (tenants) with a single instance of the software. Even though every customer has a dedicated PBX, they all share the same telvane instance for all customers cuts down operating costs significantly.</p>
  <a class="btn btn-line">LEARN MORE</a>
</div>

<div class="prod-text" style="left:89px;top:2705px;width:450px">
  <h3>Unified Communications</h3>
  <div class="tag">Available on Desktop &amp; Mobile</div>
  <p>Communicator is a Desktop &amp; Mobile Unified Communications application designed to provide business users with a set of features and benefits capable of transforming your company communications system into a real powerhouse.</p>
  <p>It is available on Panevo, Lumen OS, Korra Linux as a desktop application, and on Drift Mobile and Halo Mobile as a mobile application.</p>
  <a class="btn btn-line">LEARN MORE</a>
</div>
<div class="shot" style="left:612px;top:2690px">
  <div class="wdots"><i></i><i></i><i></i></div>
  <div class="screen" role="img" aria-label="Screenshot of the communicator app with voicemail, dial pad and contacts windows" style="height:318px;background:linear-gradient(90deg,#e9eef3 0 38%,#fff 38% 39%,#e9eef3 39% 64%,#fff 64% 65%,#eef2f6 65%)"></div>
</div>
<div class="badge" style="left:568px;top:2876px"><svg width="90" height="80" viewBox="0 0 90 80" fill="none" stroke="#1d2735" stroke-width="2.5"><rect x="6" y="8" width="62" height="44" rx="2"/><path d="M22 66h36M37 52v14"/><rect x="60" y="28" width="24" height="44" rx="3"/></svg></div>

<div class="shot" style="left:80px;top:3203px">
  <div class="wdots"><i></i><i></i><i></i></div>
  <div class="screen" role="img" aria-label="Screenshot of the access portal billing dashboard" style="height:300px;background:linear-gradient(180deg,#2b2f36 0 14%,#f1f4f7 14%)"></div>
</div>
<div class="badge" style="left:476px;top:3462px"><svg width="80" height="84" viewBox="0 0 80 84" fill="none" stroke="#1b8fd8" stroke-width="2.5"><circle cx="32" cy="20" r="14"/><path d="M6 76c0-20 12-34 26-34 6 0 11 2 15 5"/><circle cx="58" cy="62" r="12"/><circle cx="58" cy="62" r="4"/></svg></div>
<div class="prod-text" style="left:704px;top:3255px">
  <h3>Invoice &amp; Payment Platform</h3>
  <div class="tag">All pieces in one for an assertive management</div>
  <p>Access Portal is a fully-featured telecom customer portal, designed for integration with one or many CloudPBX telephony switches. Access Portal has a friendly GUI that enables efficient, automated billing, invoicing and payments, allowing you to spend less time dealing with the administration of your company and more time to SELL!</p>
  <a class="btn btn-line">LEARN MORE</a>
</div>

<a class="btn btn-line abs" style="left:517px;top:3682px;width:218px;height:52px">LOAD MORE PRODUCTS</a>

<section class="support">
  <h2>Our Support<small>We are here to help</small></h2>
  <p>Our technical support team is always available to you via phone, live chat and support ticketing system.</p>
  <a class="btn">REMOTE SUPPORT ACCESS</a>
</section>

<h2 class="section-title" style="top:4110px">Why Rivet Halvora?</h2>
<div class="abs" style="left:599px;top:4196px;width:1px;height:300px;background:var(--line)"></div>
<div class="abs" style="left:89px;top:4340px;width:1022px;height:1px;background:var(--line)"></div>
<div class="why-item" style="left:89px;top:4200px">
  <svg width="70" height="70" viewBox="0 0 70 70" fill="none" stroke="#1b8fd8" stroke-width="2"><circle cx="35" cy="35" r="10"/><path d="M35 25V8M35 45v17M25 35H8M45 35h17M28 28 16 16M42 42l12 12M42 28l12-12M28 42 16 54"/><circle cx="35" cy="6" r="3"/><circle cx="35" cy="64" r="3"/><circle cx="6" cy="35" r="3"/><circle cx="64" cy="35" r="3"/></svg>
  <div><h4>Tested and proven technologies</h4><p>Aenean sollicitudin, lorem quis bibendum auctor nisi elit consequat ipsum nec sagittis sem nibh id elit duis sed odio sit amet nibh...</p></div>
</div>
<div class="why-item" style="left:667px;top:4200px">
  <svg width="70" height="70" viewBox="0 0 70 70" fill="none" stroke="#1b8fd8" stroke-width="2"><circle cx="35" cy="38" r="25"/><path d="M35 22v16l10 8M29 6h12M35 6v7"/></svg>
  <div><h4>We do not keep you waiting</h4><p>Aenean sollicitudin, lorem quis bibendum auctor nisi elit consequat ipsum nec sagittis sem nibh id elit duis sed odio sit amet nibh...</p></div>
</div>
<div class="why-item" style="left:89px;top:4382px">
  <svg width="70" height="70" viewBox="0 0 70 70" fill="none" stroke="#1b8fd8" stroke-width="2"><circle cx="35" cy="35" r="20"/><circle cx="35" cy="35" r="5"/><path d="M35 4v16M35 50v16M4 35h16M50 35h16"/></svg>
  <div><h4>We are here to help</h4><p>Aenean sollicitudin, lorem quis bibendum auctor nisi elit consequat ipsum nec sagittis sem nibh id elit duis sed odio sit amet nibh...</p></div>
</div>
<div class="why-item" style="left:667px;top:4382px">
  <svg width="70" height="70" viewBox="0 0 70 70" fill="none" stroke="#1b8fd8" stroke-width="2"><rect x="12" y="10" width="40" height="52" rx="3"/><path d="M24 6h16v8H24zM20 28h6M20 40h6M20 52h6M30 28h14M30 40h10"/><path d="M40 54 62 30"/></svg>
  <div><h4>Solutions tailored for your business</h4><p>Aenean sollicitudin, lorem quis bibendum auctor nisi elit consequat ipsum nec sagittis sem nibh id elit duis sed odio sit amet nibh...</p></div>
</div>

<h2 class="section-title" style="top:4572px">Hardware</h2>
<span class="hw" style="left:148px">Veloran</span>
<span class="hw" style="left:330px">Quenta</span>
<span class="hw" style="left:513px">Tonvale</span>
<span class="hw" style="left:693px">Moxeri</span>
<span class="hw" style="left:877px">Sundrell</span>
<span class="hw" style="left:1060px">Arvik</span>
<div class="dots-row" style="top:4734px"><span class="on"></span><span></span><span></span></div>

<footer class="footer">
  <div class="flogo"><span class="mark"></span>Rivet Halvora</div>
  <div class="fsoc"><span></span><span></span><span></span><span></span></div>
  <div class="fcol" style="left:455px">
    <h5>Quick Links</h5>
    <div>Home</div><div>Voice</div><div>Data</div><div>Hardware</div><div>Services Request</div><div>Terms &amp; Conditions</div><div>Status</div>
  </div>
  <div class="fcol" style="left:693px">
    <h5>Resources</h5>
    <div>Company</div><div>Careers</div><div>Partner Application</div><div>Events</div><div>Expos</div><div>Our Press</div><div>Latest Blog</div>
  </div>
  <div class="fcol" style="left:894px">
    <h5>Contact Us</h5>
    <h6>Administration</h6>
    <div class="c"><i></i>admin@rivethalvora.com.au</div><div class="c"><i></i>+61 2 5550 1842</div>
    <h6 style="margin-top:14px">Accounts</h6>
    <div class="c"><i></i>accounts@rivethalvora.com.au</div><div class="c"><i></i>+61 2 5550 1842</div>
    <h6 style="margin-top:14px">Support</h6>
    <div class="c"><i></i>support@rivethalvora.com.au</div><div class="c"><i></i>+61 2 5550 1842</div>
  </div>
  <a class="totop"><svg width="16" height="16" viewBox="0 0 16 16"><path d="M8 14V2M3 7l5-5 5 5" stroke="#fff" stroke-width="2" fill="none"/></svg></a>
  <div class="copy">© Copyright 2019 · All Rights Reserved.</div>
</footer>

</body>
</html>
```